Endocrinologist needs new stationery

I have a logo from MarkForge and now need stationery with the new logo.

Address: Suite 4, 282 Falcon Street, Richmond, VIC 3121
Phone: 03 9417 2253
Fax: 03 9417 2255
Website: www.drmaylacorwen.com.au
Email: admin@drmaylacorwen.com.au

```html
<!DOCTYPE html>
<html lang="en">
<head>
<meta charset="utf-8">
<title>Dr Mayla Corwen – Letterhead</title>
<link rel="stylesheet" href="https://fonts.googleapis.com/css2?family=Lato:wght@400&family=Arimo:wght@400&display=swap">
<style>
  :root{
    --bg:#d9d9d9;
    --paper:#ffffff;
    --brand-blue:#2f6b9a;
    --brand-mauve:#7a5068;
    --ink:#111111;
    --ink-soft:#333333;
    --rule:#555555;
    --sig-fill:#ececec;
  }
  *{margin:0;padding:0;box-sizing:border-box}
  html,body{width:1200px;height:1159px;overflow:hidden;background:var(--bg)}
  .letterhead{
    position:absolute;left:205px;top:21px;width:790px;height:1117px;
    background:var(--paper);box-shadow:0 4px 18px rgba(0,0,0,.18);overflow:hidden;
  }
  .header{position:absolute;left:56px;top:56px;right:48px;height:90px;display:flex;align-items:center}
  .brand{display:flex;align-items:center;gap:10px;width:300px}
  .brand-mark{width:12px;height:12px;background:var(--brand-blue)}
  .brand-name{font-family:'Lato',sans-serif;font-weight:400;font-size:29px;color:var(--brand-blue);letter-spacing:.5px}
  .divider{width:1px;height:62px;background:var(--rule);margin:0 22px 0 8px}
  .contacts{display:grid;grid-template-columns:auto auto;column-gap:22px;row-gap:7px;
    font-family:'Lato',sans-serif;font-size:12.5px;color:var(--ink-soft);letter-spacing:.4px}
  .contact{display:flex;align-items:center;gap:8px;white-space:nowrap}
  .contact.address{grid-column:1 / 3}
  .icon{width:17px;height:17px;background:var(--brand-blue);border-radius:2px;display:flex;align-items:center;justify-content:center;flex:none}
  .icon svg{width:11px;height:11px}
  .body{position:absolute;left:190px;right:80px;top:250px;
    font-family:'Arimo',Arial,sans-serif;font-size:14px;line-height:1.22;color:var(--ink)}
  .body p{margin-bottom:38px}
  .signature{position:absolute;left:250px;top:905px;width:230px;height:70px;background:var(--sig-fill);border-radius:4px}
  .footer-band{position:absolute;bottom:0;height:14px}
  .footer-band.primary{left:0;width:575px;background:var(--brand-blue)}
  .footer-band.accent{left:585px;right:0;background:var(--brand-mauve)}
</style>
</head>
<body>
<main class="letterhead">
  <header class="header">
    <div class="brand">
      <span class="brand-mark"></span>
      <span class="brand-name">Dr Mayla Corwen</span>
    </div>
    <div class="divider"></div>
    <div class="contacts">
      <div class="contact">
        <span class="icon"><svg viewBox="0 0 24 24"><path fill="#fff" d="M6.6 10.8a15 15 0 0 0 6.6 6.6l2.2-2.2c.3-.3.7-.4 1-.2 1.1.4 2.3.6 3.6.6.6 0 1 .4 1 1V20c0 .6-.4 1-1 1A17 17 0 0 1 3 4c0-.6.4-1 1-1h3.5c.6 0 1 .4 1 1 0 1.3.2 2.5.6 3.6.1.3 0 .7-.2 1z"/></svg></span>
        03 9417 2253
      </div>
      <div class="contact">
        <span class="icon"><svg viewBox="0 0 24 24"><path fill="#fff" d="M2 4h20v16H2z" opacity=".0"/><path fill="#fff" d="M3 5h18v14H3zm2 2v.5l7 5 7-5V7l-7 5z"/></svg></span>
        admin@drmaylacorwen.com.au
      </div>
      <div class="contact">
        <span class="icon"><svg viewBox="0 0 24 24"><path fill="#fff" d="M6 3h9v5H6zM4 9h16v11H4zm3 3v2h2v-2zm4 0v2h2v-2zm4 0v2h2v-2zm-8 4v2h2v-2zm4 0v2h2v-2zm4 0v2h2v-2z"/></svg></span>
        03 9417 2255
      </div>
      <div class="contact">
        <span class="icon"><svg viewBox="0 0 24 24"><circle cx="12" cy="12" r="9" fill="none" stroke="#fff" stroke-width="2"/><path d="M3 12h18M12 3c3 3 3 15 0 18M12 3c-3 3-3 15 0 18" fill="none" stroke="#fff" stroke-width="1.6"/></svg></span>
        www.drmaylacorwen.com.au
      </div>
      <div class="contact address">
        <span class="icon"><svg viewBox="0 0 24 24"><path fill="#fff" d="M12 2a7 7 0 0 0-7 7c0 5 7 13 7 13s7-8 7-13a7 7 0 0 0-7-7zm0 9.5A2.5 2.5 0 1 1 12 6.5a2.5 2.5 0 0 1 0 5z"/></svg></span>
        Suite 4, 282 Falcon Street, Richmond, VIC 3121
      </div>
    </div>
  </header>

  <section class="body">
    <p>Lorem ipsum dolor sit amet, consectetur adipiscing elit. Donec fringilla neque euismod volutpat cursus. Vestibulum ac pretium orci, consequat elementum velit. Etiam bibendum purus ac augue finibus volutpat. Vestibulum justo nisl.</p>
    <p>Lorem ipsum dolor sit amet, consectetur adipiscing elit. Donec fringilla neque euismod volutpat cursus. Vestibulum ac pretium orci, consequat elementum velit. Etiam bibendum purus ac augue finibus volutpat. Vestibulum justo nisl.</p>
    <p>Lorem ipsum dolor sit amet, consectetur adipiscing elit. Donec fringilla neque euismod volutpat cursus. Vestibulum ac pretium orci, consequat elementum velit. Etiam bibendum purus ac augue finibus volutpat. Vestibulum justo nisl, gravida aliquet sollicitudin ut, finibus vitae mi. Praesent aliquet scelerisque blandit. Sed id varius lacus, id tristique sem. Fusce et lobortis leo. Aliquam mollis pellentesque magna, condimentum ullamcorper ex ullamcorper non. Morbi ultricies nunc eu tellus dignissim, eget venenatis dolor ullamcorper. Etiam dolor eros, iaculis at ultricies nec, volutpat nec orci. Vivamus tincidunt rutrum sapien, ac porttitor mauris tristique nec.</p>
    <p>Lorem ipsum dolor sit amet, consectetur adipiscing elit. Donec fringilla neque euismod volutpat cursus. Vestibulum ac pretium orci, consequat elementum velit. Etiam bibendum purus ac augue finibus volutpat. Vestibulum justo nisl, gravida aliquet sollicitudin ut, finibus vitae mi. Praesent aliquet scelerisque blandit. Sed id varius lacus, id tristique sem. Fusce et lobortis leo. Aliquam mollis pellentesque magna, condimentum ullamcorper ex ullamcorper non. Morbi ultricies nunc eu tellus dignissim, eget venenatis dolor ullamcorper. Etiam dolor eros, iaculis at ultricies nec, volutpat nec orci. Vivamus tincidunt rutrum sapien, ac porttitor mauris tristique nec.</p>
    <p>Lorem ipsum dolor sit amet, consectetur adipiscing elit. Donec fringilla neque euismod volutpat cursus. Vestibulum ac pretium orci, consequat elementum velit. Etiam bibendum purus ac augue finibus volutpat. Vestibulum justo nisl.</p>
  </section>

  <div class="signature" role="img" aria-label="Handwritten signature of Theo J. Marsden"></div>

  <div class="footer-band primary"></div>
  <div class="footer-band accent"></div>
</main>
</body>
</html>
```